依頼詳細
そこを通れば見落とさずに、入ってこれるような、目立つ看板で、それなりにカッコいいけど親しみやすい雰囲気がいいです。
サイズは縦長で、縦360cm×横90cmです。
記載項目
タイドオービット、Tide Orbit、株式会社アウルリード、Owl-Reed
希望イメージ
シンプル 複雑
単色 カラフル
暗い 明るい
日常 高級
遊び心 厳粛
未来的 伝統的
女性的 男性的
希望する色
赤系、緑系、黄・オレンジ系
納品ファイル
• 高解像度JPG (.jpg)
• イラストレーター形式 (.ai)
• フォトショップ形式 (.psd)
補足説明
イメージカラーは明るい緑とオレンジです。
会社のロゴは添付の通りなので、そのOwl-Reedの部分を、Tide Orbit/タイドオービットにして、その下に「Produced by Owl-Reed Inc」というように入れて使ってもらいたいです。
ロゴを添付します

```html
<!DOCTYPE html>
<html lang="ja">
<head>
<meta charset="utf-8">
<title>Tide Orbit サイン</title>
<link rel="stylesheet" href="https://fonts.googleapis.com/css2?family=Noto+Sans+JP:wght@500;700;900&display=swap">
<style>
  :root {
    --backdrop: #ececec;
    --sign-dark: #2b2120;
    --sign-green: #35a94a;
    --accent-orange: #ee8a25;
    --ghost-type: #4b4546;
    --type-white: #ffffff;
  }
  html, body {
    margin: 0;
    padding: 0;
    width: 1200px;
    height: 3836px;
    overflow: hidden;
    background: var(--backdrop);
  }
  .sign {
    position: absolute;
    left: 252px;
    top: 192px;
    width: 816px;
    height: 3428px;
    background: var(--sign-dark);
    overflow: hidden;
  }
  .sign__graphics {
    position: absolute;
    inset: 0;
    width: 816px;
    height: 3428px;
  }
  .sign__wave { fill: var(--sign-green); }
  .sign__ghost-name {
    fill: var(--ghost-type);
    font-family: "Noto Sans JP", sans-serif;
    font-weight: 700;
    font-size: 560px;
    letter-spacing: -8px;
  }
  .brand {
    position: absolute;
    left: 0;
    right: 0;
    top: 1230px;
    text-align: center;
    font-family: "Noto Sans JP", sans-serif;
  }
  .brand__name {
    display: inline-flex;
    align-items: center;
    gap: 28px;
    margin: 0;
    color: var(--type-white);
    font-weight: 700;
    font-size: 116px;
    line-height: 1;
    letter-spacing: -2px;
  }
  .brand__dot {
    width: 64px;
    height: 64px;
    border-radius: 50%;
    background: var(--accent-orange);
  }
  .brand__kana {
    margin: 44px 0 0;
    color: var(--type-white);
    font-weight: 500;
    font-size: 58px;
    line-height: 1;
  }
  .brand__producer {
    margin: 26px 0 0;
    color: var(--type-white);
    font-weight: 900;
    font-size: 36px;
    letter-spacing: 1px;
    line-height: 1;
  }
</style>
</head>
<body>
  <div class="sign">
    <svg class="sign__graphics" viewBox="0 0 816 3428" aria-hidden="true">
      <path class="sign__wave" d="M0,0 H140 C60,500 0,900 30,1300 C60,1800 200,2300 190,2700 C180,3100 100,3300 90,3428 H0 Z"/>
      <text class="sign__ghost-name" transform="translate(400,90) rotate(90)">Tide Orbit</text>
    </svg>
    <div class="brand">
      <p class="brand__name"><span class="brand__dot"></span>Tide Orbit</p>
      <p class="brand__kana">タイドオービット</p>
      <p class="brand__producer">Produced by Owl-Reed Inc</p>
    </div>
  </div>
</body>
</html>
```